Crestline Lending Group Business Cards

We are looking to revamp the current business cards each of our locations uses. We are a lending company that specializes in personal loans, title loans, and tax services. We have locations in New Mexico, Texas, and Oklahoma.

We would like a cleaner, sleeker look while still highlighting what we offer. Title Loans, Personal Loans & Tax Services. We also want to include our referral fee somewhere on the card. We would like to see an English option as well as a Spanish option for the cards.

PLEASE NOTE: Some business cards do not include the employee's name but just the store's location, while others will include both.

These are double-sided business cards, and we would like to see proof if possible. I have included proofs of our current business cards for you to review below, as well as our company logo. Feel free to get creative with the logo, etc! Colors should match the logo; however, you do not need to use all of our logo colors if you don't want to.

```html
<!DOCTYPE html>
<html lang="en">
<head>
<meta charset="utf-8">
<title>Crestline Lending Group – Business Cards</title>
<link href="https://fonts.googleapis.com/css2?family=Barlow:wght@400;500;600&family=Barlow+Semi+Condensed:wght@500;600&display=swap" rel="stylesheet">
<style>
  :root {
    --brand-green: #34c01f;
    --deep-green: #1f6b12;
    --brand-red: #c4040a;
    --white: #ffffff;
    --paper: #ffffff;
  }
  html, body { margin: 0; padding: 0; overflow: hidden; background: var(--paper); }
  .sheet {
    position: relative; width: 1200px; height: 849px; overflow: hidden;
    background: var(--paper); font-family: "Barlow", Arial, sans-serif;
  }

  /* Front card */
  .card-front {
    position: absolute; left: 181px; top: 209px; width: 389px; height: 259px;
    background: var(--brand-green); color: var(--white);
  }
  .card-front .brand-dot {
    position: absolute; left: 60px; top: 40px; width: 56px; height: 56px;
    border-radius: 50%; background: var(--brand-red);
  }
  .card-front .services {
    position: absolute; left: 163px; top: 71px; font-size: 9px; font-weight: 500;
    color: var(--deep-green); white-space: nowrap;
  }
  .card-front .services .sep { color: var(--brand-red); }
  .card-front .brand-name {
    position: absolute; left: 163px; top: 90px; font-size: 20px; font-weight: 600;
    line-height: 1; color: var(--white); white-space: nowrap;
  }
  .card-front .web {
    position: absolute; left: 163px; width: 193px; text-align: right; top: 122px;
    font-size: 11px; font-weight: 500; color: var(--deep-green); white-space: nowrap;
  }
  .contact-list {
    position: absolute; left: 163px; top: 141px; margin: 0; padding: 0; list-style: none;
    font-size: 15px; font-weight: 500; letter-spacing: 0.3px;
  }
  .contact-list li { position: relative; padding-left: 9px; height: 20.5px; line-height: 20px; white-space: nowrap; }
  .contact-list li::before {
    content: ""; position: absolute; left: 0; top: 11px; width: 4px; height: 4px;
    border-radius: 50%; background: var(--deep-green);
  }

  /* Back card */
  .card-back {
    position: absolute; left: 607px; top: 260px; width: 389px; height: 260px;
    background: var(--brand-red); overflow: hidden;
  }
  .card-back .burst { position: absolute; left: 0; top: 0; }
  .card-back .brand-name {
    position: absolute; left: 26px; top: 44px; font-size: 11px; font-weight: 600;
    color: var(--white); white-space: nowrap;
  }
  .card-back .web {
    position: absolute; left: 52px; top: 58px; font-size: 4px; color: var(--brand-red);
  }
  .offer {
    position: absolute; left: 157px; top: 68px; color: var(--white);
    font-family: "Barlow Semi Condensed", Arial Narrow, sans-serif; font-weight: 500;
  }
  .offer .lead { font-size: 16px; line-height: 18px; letter-spacing: 0.6px; }
  .offer .lead-2 { font-size: 19px; line-height: 18px; letter-spacing: 0.4px; }
  .offer .amount {
    position: absolute; left: -62px; top: 30px; font-size: 112px; font-weight: 600;
    line-height: 1; letter-spacing: -1px; white-space: nowrap;
  }

  /* Brand lockup */
  .lockup { position: absolute; left: 0; top: 0; width: 1200px; height: 849px; pointer-events: none; }
  .lockup .brand-dot {
    position: absolute; left: 385px; top: 630px; width: 56px; height: 56px;
    border-radius: 50%; background: var(--brand-red);
  }
  .lockup .brand-name {
    position: absolute; left: 452px; top: 652px; font-size: 32px; font-weight: 600;
    line-height: 1; color: var(--brand-green); white-space: nowrap;
  }
  .lockup .web {
    position: absolute; left: 400px; width: 400px; top: 702px; text-align: right;
    font-size: 17px; font-weight: 500; color: var(--brand-red); white-space: nowrap;
  }
  .lockup .services {
    position: absolute; left: 401px; top: 727px; font-size: 20px; font-weight: 500;
    color: var(--brand-green); letter-spacing: 0.4px; white-space: nowrap;
  }
</style>
</head>
<body>
<main class="sheet">

  <section class="card-front" aria-label="Business card front">
    <span class="brand-dot"></span>
    <div class="services">Title Loans <span class="sep">|</span> Personal Loans <span class="sep">|</span> Tax Services</div>
    <div class="brand-name">Crestline Lending Group</div>
    <div class="web">www.crestlinelending.com</div>
    <ul class="contact-list">
      <li>218 Ridgeview Avenue</li>
      <li>Harlan, Texas 79412</li>
      <li>(505) 555-0148</li>
      <li>abcde@crestlinelending.com</li>
    </ul>
  </section>

  <section class="card-back" aria-label="Business card back, referral offer">
    <svg class="burst" width="389" height="260" viewBox="0 0 389 260" aria-hidden="true">
      <path fill="var(--brand-green)" d="
        M116 2
        Q170 52 203 24
        Q228 70 306 36
        Q262 110 319 145
        Q292 170 332 218
        Q280 205 262 244
        Q230 232 203 260
        L186 260
        Q170 225 116 228
        Q125 180 44 185
        Q110 140 79 98
        Q132 75 116 2 Z"/>
    </svg>
    <div class="brand-name">Crestline Lending Group</div>
    <div class="web">www.crestlinelending.com</div>
    <div class="offer">
      <div class="lead">REFER A FRIEND</div>
      <div class="lead-2">GET UP TO</div>
      <div class="amount">$100</div>
    </div>
  </section>

  <section class="lockup" aria-label="Brand lockup">
    <span class="brand-dot"></span>
    <span class="brand-name">Crestline Lending Group</span>
    <div class="web">www.crestlinelending.com</div>
    <div class="services">Title Loans | Personal Loans | Tax Services</div>
  </section>

</main>
</body>
</html>
```